Create a pouch design for a new sports supplement product

Dimensions are 235mm (width) x 335mm (length) x 110mm (gusset)
File 1 - Extension of design brief please read both briefs
File 2 - Is 2 potential pouches this is just to give you a better example of size the dimensions are for the pouch on the right. This picture is not to give you design ideas as I am not very keen on either of these designs.
We need a design to be printed onto the pouches of our whey protein product. The brand name is 'Stellar Fuelworks' and needs to be displayed on the packaging either just writing or a simple logo design. I am not the most creative person in the world but have put together a more detailed brief listing some of the key information that needs to be included on the pouch (See attachment) Please feel free if you have experience of this the sports supplement market or have different ideas then please feel free to explore them.
The pouch would either be printed straight onto the pouch, or possibly just a printed label (front & back) to be stuck onto the pouch. Please design either or both.
Open to different colour schemes. Design has to be modern looking and eye-catching.
Some key points;
High quality whey protein concentrate
All Natural
Soy free
Great tasting
Please google image search 'protein pouches' to see other designs if your not familiar with the sports supplement market.
Any questions feel free to ask.
Updates
Hi, Thanks for all your design! I am really busy at the moment so haven't had chance to give feedback and have a proper look through all the designs. I have extended the time frame to give myself chance to give proper feedback and see any changes needed. Expect feedback sunday at the latest, and I will be pick a design early next week.
Target Market(s)
Sports supplement market. Product is a whey protein shake
Industry/Entity Type
Nutrition
Look and feel
Each slider illustrates characteristics of the customer's brand and the style your logo design should communicate.

```html
<!DOCTYPE html>
<html lang="en">
<head>
<meta charset="utf-8">
<title>Stellar Fuelworks – Natural Whey Protein Pouch</title>
<link rel="stylesheet" href="https://fonts.googleapis.com/css2?family=Jost:wght@300;400&display=swap">
<style>
  :root {
    --ink: #231f20;
    --signal-red: #ed1c2e;
    --page: #ffffff;
    --pouch: #fcfcfc;
    --edge: #e2e2e2;
  }
  * { margin: 0; padding: 0; box-sizing: border-box; }
  html, body {
    width: 942px;
    height: 1200px;
    overflow: hidden;
    background: var(--page);
    font-family: "Jost", "Futura", sans-serif;
    color: var(--ink);
  }
  .pouch-front {
    position: absolute;
    left: 132px;
    top: 113px;
    width: 674px;
    height: 966px;
    background: var(--pouch);
    border: 1px solid var(--edge);
  }
  .tear-notch {
    position: absolute;
    top: 27px;
    right: 45px;
    font-size: 16px;
    font-weight: 400;
    letter-spacing: 0.4px;
  }
  .brand-name {
    position: absolute;
    top: 136px;
    left: 0;
    width: 100%;
    text-align: center;
    font-size: 90px;
    font-weight: 300;
    line-height: 1;
    letter-spacing: -0.5px;
  }
  .product-name {
    position: absolute;
    top: 236px;
    left: 0;
    width: 100%;
    text-align: center;
    font-size: 50px;
    font-weight: 400;
    line-height: 1;
    letter-spacing: 5.5px;
    color: var(--signal-red);
  }
  .band-field {
    position: absolute;
    left: 0;
    background: linear-gradient(180deg, var(--ink) 0%, var(--signal-red) 100%);
    opacity: 0.9;
  }
  .band-field--upper { top: 317px; width: 674px; height: 189px; }
  .band-field--lower { top: 704px; width: 674px; height: 87px; }
  .benefits {
    position: absolute;
    top: 531px;
    left: 0;
    width: 100%;
    text-align: center;
    font-size: 26px;
    font-weight: 400;
    line-height: 42px;
  }
  .benefits .dot {
    display: inline-block;
    width: 10px;
    height: 10px;
    margin: 0 10px 3px;
    border-radius: 50%;
    background: var(--signal-red);
  }
  .pack-details {
    position: absolute;
    top: 812px;
    left: 0;
    width: 100%;
    text-align: center;
    font-size: 29px;
    font-weight: 400;
    line-height: 44px;
    letter-spacing: 1px;
  }
  .pack-details .flavour { color: var(--signal-red); }
</style>
</head>
<body>
  <main class="pouch-front">
    <p class="tear-notch">Tear here &amp; Reseal</p>

    <h1 class="brand-name">Stellar Fuelworks</h1>
    <h2 class="product-name">Natural Whey Protein</h2>

    <div class="band-field band-field--upper" role="img" aria-label="Decorative field of horizontal black and red stripes"></div>

    <div class="benefits">
      <p>No Artificial Flavours<span class="dot"></span>Excellent Amino Acid Profile</p>
      <p>80% High Quality Protein Content<span class="dot"></span>Soy Free</p>
    </div>

    <div class="band-field band-field--lower" role="img" aria-label="Decorative field of horizontal black and red stripes"></div>

    <div class="pack-details">
      <p class="flavour">Strawberry Flavour</p>
      <p class="servings">30 Servings</p>
      <p class="net-weight">909g</p>
    </div>
  </main>
</body>
</html>
```